Geschäftspapiere Ingenieurgesellschaft
Sehr schnelle Reaktionszeit. Sofort auf Wünsche eingegangen. Und Verena war sehr geduldig mit mir.
Zielgruppe
Wir sind ein Ingenieurbüro für Spezialtiefbau mit der Rechtsform PartG mbB. Daher ist unsere Bezeichnung ziemlich stringent vorgegeben. 'BRANDOWER-HESSE PartG mbB, Beratende Ingenieure im Spezialtiefbau'
Unsere Kunden sind öffentliche Auftraggeber, Architekten, Bauingenieure, aber auch privatwirtschaftliche Auftraggeber und Privatleute.
Aufgabenstellung
Wir sind im Design nicht festgelegt, auch in den Farben sind wir relativ frei. Pink und lila sollte es vielleicht nicht gerade sein :-) Ansonsten sind Ingenieure geradlinig, symmetrisch und mathematisch orientiert.
In der Anlage sind unsere bisherigen Briefpapiere und VC beispielhaft, dienen nur der Info.
#03.02.2020: Auf Grund der mäßigen Beteiligung möchte ich das Briefing ergänzen.
Wir benötigen ein Briefpapier DIN A4 mit den erforderlichen Angaben:
- Firmenname
- Anschrift
- Kommunikationswege
- Bankverbindung
etc.
Zudem benötigen wir eine Visitenkarte (für zwei verschiedene Personen)
Schön wäre ein Symbol mit dem man den Spezialtiefbau verbindet, z.B. ein Pfeil nach unten.
Auf www.ib-brandower.example und www.ib-hesse.example können Sie unsere bisherigen Designs betrachten, beide auch hier in entwurfsplatz.example erstellt. !!!!!!!!!!Das neue Design soll sich in Farbe und Layout von den anderen unterscheiden.
Mögliche Farbe wäre basaltgrau bzw. grau allgemein. Visitenkarte das Symbol auf der Vorderseite und die Infos auf der Innenseite.
-----Wir haben mit Absicht wenig Vorgaben gemacht, um die Ideen der Designer nicht all zu sehr einzuschränken. Kommt wohl nicht gut an?-----

```html
<!DOCTYPE html>
<html lang="de">
<head>
<meta charset="utf-8">
<title>BRANDOWER HESSE PartG mbB – Visitenkarte</title>
<link rel="stylesheet" href="https://fonts.googleapis.com/css2?family=Open+Sans:wght@400;600;700&display=swap">
<style>
  :root {
    --basalt: #4b5155;
    --blue: #0a86d0;
    --white: #ffffff;
    --ink: #1d1f21;
    --muted: #55595c;
    --stage: #e4e7ea;
  }
  * { box-sizing: border-box; margin: 0; padding: 0; }
  html, body { width: 1200px; height: 900px; overflow: hidden; }
  body {
    background: var(--stage);
    font-family: "Open Sans", Arial, sans-serif;
    display: flex;
    align-items: center;
    justify-content: center;
    gap: 60px;
  }
  .card {
    position: relative;
    width: 510px;
    height: 310px;
    box-shadow: 0 6px 20px rgba(0,0,0,0.18);
    overflow: hidden;
  }

  /* Vorderseite */
  .card--back {
    background: var(--basalt);
    color: var(--white);
  }
  .back-mark {
    position: absolute;
    top: 96px;
    left: 0;
    right: 0;
    display: flex;
    align-items: center;
    justify-content: center;
    gap: 14px;
  }
  .back-mark__square {
    width: 34px;
    height: 34px;
    background: var(--blue);
  }
  .back-mark__name {
    font-weight: 600;
    font-size: 30px;
    line-height: 1.05;
    letter-spacing: 0.5px;
    color: var(--white);
  }
  .back-url {
    position: absolute;
    bottom: 58px;
    left: 0;
    right: 0;
    text-align: center;
    font-size: 14px;
    letter-spacing: 0.3px;
  }

  /* Innenseite */
  .card--front {
    background: var(--white);
    color: var(--ink);
  }
  .firm {
    position: absolute;
    top: 30px;
    right: 34px;
    text-align: right;
  }
  .firm__name {
    font-weight: 600;
    font-size: 30px;
    line-height: 1;
    color: var(--blue);
    letter-spacing: 0.5px;
  }
  .firm__name span { display: block; }
  .firm__tagline {
    margin-top: 8px;
    font-size: 11px;
    letter-spacing: 0.6px;
    color: var(--muted);
    text-transform: uppercase;
  }
  .address {
    position: absolute;
    left: 40px;
    top: 140px;
    font-size: 13px;
    line-height: 1.45;
  }
  .contact {
    position: absolute;
    left: 40px;
    top: 196px;
    list-style: none;
    font-size: 13px;
    line-height: 1.55;
  }
  .contact li { display: flex; align-items: center; gap: 8px; }
  .contact svg { width: 12px; height: 12px; flex: none; }
  .person {
    position: absolute;
    right: 34px;
    top: 172px;
    text-align: right;
  }
  .person__name {
    font-weight: 700;
    font-size: 19px;
    color: var(--blue);
  }
  .person__title {
    font-size: 13px;
    margin-top: 4px;
  }
  .band {
    position: absolute;
    left: 0;
    right: 0;
    bottom: 26px;
    height: 30px;
    background: var(--blue);
    color: var(--white);
    font-size: 13px;
    display: flex;
    align-items: center;
    justify-content: center;
    letter-spacing: 0.3px;
  }
</style>
</head>
<body>

  <section class="card card--back" aria-label="Vorderseite">
    <div class="back-mark">
      <div class="back-mark__square"></div>
      <div class="back-mark__name">BRANDOWER<br>HESSE</div>
    </div>
    <p class="back-url">www.brandower-hesse.example</p>
  </section>

  <section class="card card--front" aria-label="Innenseite">
    <header class="firm">
      <p class="firm__name"><span>BRANDOWER</span><span>HESSE PartG mbB</span></p>
      <p class="firm__tagline">Beratende Ingenieure im Spezialtiefbau</p>
    </header>

    <address class="address" style="font-style:normal">
      Lindenweg 12<br>
      56000 Talheim/Lahn
    </address>

    <ul class="contact">
      <li>
        <svg viewBox="0 0 12 12" aria-hidden="true"><rect x="3" y="0.5" width="6" height="11" rx="1" fill="none" stroke="var(--blue)" stroke-width="1.2"/><line x1="5" y1="9.5" x2="7" y2="9.5" stroke="var(--blue)" stroke-width="1"/></svg>
        01234-5678901
      </li>
      <li>
        <svg viewBox="0 0 12 12" aria-hidden="true"><rect x="0.5" y="2" width="11" height="8" fill="var(--blue)"/><polyline points="0.5,2 6,6.5 11.5,2" fill="none" stroke="var(--white)" stroke-width="1"/></svg>
        mh@brandower-hesse.example
      </li>
    </ul>

    <div class="person">
      <p class="person__name">Matthias Hesse</p>
      <p class="person__title">Dipl.-Ing. (FH)</p>
    </div>

    <footer class="band">www.brandower-hesse.example</footer>
  </section>

</body>
</html>
```